Visitenkarten-Design für Malermeisterbetrieb
Zielgruppe
Ich habe einen Malermeisterbetrieb und unsere Hauptaufgabe besteht im Fassadenanstrich, Fußbodenlegearbeiten und Tapezier- und Anstricharbeiten. Als Zielgruppe erreichen wir Verwaltungsfirmen, Privatkundschaft und Bauträger.
Aufgabenstellung
Visitenkarten bitte so ähnlich wie die alten Vorlagen (siehe Angang) bearbeiten aber die neuen Bilder (ebenfalls im Angang) einfügen

```html
<!DOCTYPE html>
<html lang="de">
<head>
<meta charset="utf-8">
<title>Visitenkarte Malermeisterbetrieb</title>
<link href="https://fonts.googleapis.com/css2?family=Open+Sans:wght@600;700&family=Great+Vibes&display=swap" rel="stylesheet">
<style>
  :root{
    --stage:#e4e7ea;
    --card-blue:#93d4df;
    --card-deep:#4fb3c7;
    --panel-light:#ffffff;
    --ink:#1f2326;
    --accent-red:#d13c1e;
    --band-orange:#ffa33a;
    --band-red:#ef5b3e;
    --photo-warm:#8a5a3c;
    --photo-grey:#a9a9a4;
  }
  *{margin:0;padding:0;box-sizing:border-box}
  html,body{width:1200px;height:900px;overflow:hidden;background:var(--stage)}
  .stage{position:relative;width:1200px;height:900px}
  .card{position:absolute;top:280px;width:540px;height:340px;border-radius:22px;overflow:hidden;
        box-shadow:0 6px 18px rgba(0,0,0,.18);font-family:"Open Sans",sans-serif;color:var(--ink)}
  .card--front{left:40px}
  .card--back{left:620px}
  .card-art{position:absolute;inset:0;width:100%;height:100%}
  .trade{position:absolute;right:34px;top:18px;font-weight:700;font-size:22px;letter-spacing:.2px}
  .owner{position:absolute;right:40px;top:48px;font-family:"Great Vibes",cursive;font-size:62px;
         color:var(--accent-red);line-height:1}
  .address{position:absolute;right:34px;top:160px;font-weight:700;font-size:15px;line-height:1.35;text-align:left}
  .phones{position:absolute;left:262px;top:210px;font-weight:700;font-size:15px;line-height:1.4}
  .email{position:absolute;left:180px;top:286px;font-weight:600;font-size:13px}
  .web{position:absolute;left:170px;top:304px;font-weight:700;font-size:19px;color:var(--accent-red)}
  .services{position:absolute;left:0;top:0;width:100%;height:100%}
  .service{position:absolute;height:44px;display:flex;align-items:center;font-weight:600;font-size:17px;color:var(--ink)}
  .service b{font-size:34px;font-weight:700;margin-right:2px;line-height:1}
</style>
</head>
<body>
<div class="stage">

  <section class="card card--front">
    <svg class="card-art" viewBox="0 0 540 340" aria-hidden="false">
      <defs>
        <linearGradient id="frontPanel" x1="0" y1="1" x2="1" y2="0">
          <stop offset="0" stop-color="#ffffff"/>
          <stop offset=".45" stop-color="#d8f0f4"/>
          <stop offset="1" stop-color="#4fb3c7"/>
        </linearGradient>
        <linearGradient id="frontPhoto" x1="0" y1="0" x2="1" y2="1">
          <stop offset="0" stop-color="#6e3a2a"/>
          <stop offset=".55" stop-color="#a8714a"/>
          <stop offset="1" stop-color="#e7dcc8"/>
        </linearGradient>
      </defs>
      <rect width="540" height="340" fill="var(--card-blue)"/>
      <path role="img" aria-label="Foto eines renovierten Wohnraums mit Tapete, Tür und Regal"
            d="M0,92 C90,58 200,44 300,46 L300,118 L270,118 L270,300 C170,296 80,300 0,312 Z"
            fill="url(#frontPhoto)"/>
      <path d="M270,118 L540,118 L540,238 C450,290 360,306 270,300 Z" fill="url(#frontPanel)"/>
    </svg>
    <div class="trade">Malermeisterbetrieb</div>
    <div class="owner">Jorben Kast</div>
    <div class="address">Lindenweg 7<br>39120 Hollstedt</div>
    <div class="phones">Tel.: 039471 520384<br>Fax: 039471 52039<br>Mobil: 01579 2846630</div>
    <div class="email">E-Mail: jorbenkast@maler-kast.de</div>
    <div class="web">www.malermeister-kast.de</div>
  </section>

  <section class="card card--back">
    <svg class="card-art" viewBox="0 0 540 340">
      <defs>
        <linearGradient id="backBg" x1="0" y1="1" x2="1" y2="0">
          <stop offset="0" stop-color="#ffffff"/>
          <stop offset=".4" stop-color="#cdeef3"/>
          <stop offset="1" stop-color="#4fb3c7"/>
        </linearGradient>
        <linearGradient id="backPhoto" x1="0" y1="0" x2="1" y2="1">
          <stop offset="0" stop-color="#b7b8b2"/>
          <stop offset=".6" stop-color="#8d8b82"/>
          <stop offset="1" stop-color="#7a5430"/>
        </linearGradient>
        <linearGradient id="band" x1="0" y1="0" x2="1" y2="0">
          <stop offset="0" stop-color="var(--band-red)"/>
          <stop offset=".5" stop-color="var(--band-orange)"/>
          <stop offset="1" stop-color="var(--band-red)"/>
        </linearGradient>
      </defs>
      <rect width="540" height="340" fill="var(--card-blue)"/>
      <path d="M300,0 H540 V340 H70 C110,180 190,90 300,60 Z" fill="url(#backBg)"/>
      <path role="img" aria-label="Foto eines Badezimmers mit gemusterter Tapete"
            d="M0,0 H300 V60 C190,90 110,180 70,340 H0 Z" fill="url(#backPhoto)" transform="translate(-10,-10) scale(1.0)"/>
      <path d="M0,0 H290 V50 C180,80 100,170 60,340 H0 Z" fill="url(#backPhoto)"/>
      <rect x="300" y="88" width="226" height="44" fill="url(#band)"/>
      <rect x="270" y="144" width="246" height="44" fill="url(#band)"/>
      <rect x="238" y="200" width="270" height="44" fill="url(#band)"/>
    </svg>
    <div class="services">
      <div class="service" style="left:310px;top:88px"><b>F</b>assadenanstrich</div>
      <div class="service" style="left:280px;top:144px"><b>F</b>ußbodenlegearbeiten</div>
      <div class="service" style="left:248px;top:200px"><b>T</b>apezier - u.Anstricharbeiten</div>
    </div>
  </section>

</div>
</body>
</html>
```